Business Card design for a mobile solutions company

- we are a mobile telecommunications company focusing on mobile content and solutions
- we are based in Malaysia however operate a regional business
- attached is our company logo and current business card design
- please try to incorporate the "cubes" into the design

our company philosophy is dynamic and outgoing. we are a lean team of less than 50, but we have strong roots in the mobile industry in Asia and we like to challenge ourselves by taking on larger projects.

we love joint ventures and working with partners to find the right solutions for our clients

*please feel free to modify our logo (typeface etc)
**we would like to keep the 3 cube design for the logo, but I would love to see different versions of it

some of the designs are great and I think our logo (especially the typeface used for the words) doesn't look good. please feel free to update the logo but try to keep the cubes, you are free to modify the cubes and update them.

Reason: looking for more design please

Industry/Entity Type

Telecommunications

Font styles to use
Sans Serif

```html
<!DOCTYPE html>
<html lang="en">
<head>
<meta charset="utf-8">
<title>Nova Reach – Business Card</title>
<link rel="stylesheet" href="https://fonts.googleapis.com/css2?family=PT+Sans:wght@400;700&display=swap">
<style>
  :root {
    --page: #ffffff;
    --card-light: #ddd8d8;
    --card-dark: #c4bdbd;
    --ink: #111111;
    --rule: #222222;
    --accent: #2f7fc4;
  }
  html, body {
    margin: 0;
    padding: 0;
    width: 1200px;
    height: 1000px;
    overflow: hidden;
    background: var(--page);
    font-family: "PT Sans", Arial, sans-serif;
    color: var(--ink);
  }
  .stage {
    position: relative;
    width: 1200px;
    height: 1000px;
  }
  .card {
    position: absolute;
    left: 236px;
    width: 730px;
    height: 366px;
    overflow: hidden;
  }
  .card--front { top: 92px; }
  .card--back { top: 548px; }
  .card__pattern {
    position: absolute;
    inset: 0;
    background: linear-gradient(180deg, var(--card-light) 0%, var(--card-dark) 100%);
  }
  .brand {
    position: absolute;
    left: 206px;
    top: 157px;
    display: flex;
    align-items: center;
    gap: 18px;
  }
  .brand__mark {
    width: 44px;
    height: 44px;
    background: var(--accent);
  }
  .brand__name {
    margin: 0;
    font-weight: 700;
    font-size: 46px;
    line-height: 1;
    letter-spacing: 0.5px;
  }
  .person {
    position: absolute;
    right: 362px;
    top: 112px;
    text-align: right;
  }
  .person__name {
    margin: 0;
    font-weight: 400;
    font-size: 52px;
    line-height: 1;
  }
  .person__role {
    margin: 2px 0 18px;
    font-size: 19px;
    line-height: 1.2;
  }
  .person__contact {
    margin: 0;
    font-size: 16px;
    line-height: 22px;
  }
  .divider {
    position: absolute;
    left: 415px;
    top: 100px;
    width: 1px;
    height: 200px;
    background: var(--rule);
  }
  .address {
    position: absolute;
    left: 460px;
    top: 124px;
    margin: 0;
    font-style: normal;
    font-size: 19px;
    line-height: 24.5px;
  }
</style>
</head>
<body>
<main class="stage">
  <section class="card card--front">
    <div class="card__pattern" role="img" aria-label="Grey honeycomb pattern of hexagonal cubes"></div>
    <div class="brand">
      <span class="brand__mark"></span>
      <h1 class="brand__name">NOVA REACH</h1>
    </div>
  </section>

  <section class="card card--back">
    <div class="card__pattern" role="img" aria-label="Grey honeycomb pattern of hexagonal cubes"></div>
    <div class="person">
      <h2 class="person__name">Adrian Teoh</h2>
      <p class="person__role">Chief Marketing Officer</p>
      <p class="person__contact">+60 3 418 2765<br>+62 812 7654301<br>adrian@novareach.com.my</p>
    </div>
    <div class="divider"></div>
    <address class="address">
      Nova Reach SDN BHD<br>
      Unit 5-1, Level 2 Block 4<br>
      The Meridian<br>
      Cyber Park No.12<br>
      Jalan Seroja<br>
      50450 Kuala Lumpur
    </address>
  </section>
</main>
</body>
</html>
```